Website Design for my CNC machine Shop.

I need a new website for my Machining Company.

It can be a simple website that acts more like an "Online Business card" I has to highlight the services I provide and give Companies the confidence to engage my services.

I needs it to be a really modern or even a little futuristic promoting my Company.

I have just moved locations and have renovated the premises and would be great to let everyone know along with a new website.

If you can help with linking it to search engines to help get more exposure that would be great.

It needs to accommodate the three main services I provide which will include capacities of each machine (within that service) and maybe a couple images.
CNC Machining (5-axis, 3-axis)
EDM Wire cutting
3D Metal Printing
Along with home page and Contact page

I have two websites and you can use the txt from either/combination of these.
www.korvaltooling.com.au
(no longer do Laser Marking and etching but now do 3D metal Printing)
www.tarnquill.com.au

Happy to chat further with the designer

Company logo's provided.

For Images: I am happy to use Glimmerbay and can purchase any images you like
EDM Wire cut
https://www.glimmerbay-pics.com/search/edm-wire-cutting

CNC Machining:
https://www.glimmerbay-pics.com/search/vertical-cnc-machining
Don't use any with engines or motor vehicle parts

3D metal Printing
https://www.glimmerbay-pics.com/search/slm-metal-printing

Target Market(s)

Defence, Aerospace, Medical, HIgh Precision

Industry/Entity Type

Mechanical Engineering

Coding

Coded - Design and coding required

Number of Pages Required

5+ page

Requirements
Must have
• Home page, 3 services, Contacts. Can add image to each of the services

```html
<!DOCTYPE html>
<html lang="en">
<head>
<meta charset="utf-8">
<title>Korval CNC Machining Industrial</title>
<link rel="stylesheet" href="https://fonts.googleapis.com/css2?family=Poppins:wght@400;500;600;700&display=swap">
<style>
:root{
  --green:#45c087;
  --green-soft:#8fdcb7;
  --mint:#e9faf2;
  --navy:#1b3246;
  --navy-deep:#152a3b;
  --ink:#17232e;
  --text:#333b42;
  --card:#f3f4f5;
  --white:#ffffff;
}
*{margin:0;padding:0;box-sizing:border-box}
html,body{width:1200px;height:4124px;overflow:hidden;background:var(--white)}
body{font-family:'Poppins',sans-serif;color:var(--text);position:relative}
.abs{position:absolute}
.btn{position:absolute;background:var(--green);color:var(--white);border-radius:5px;font-size:12.5px;font-weight:500;display:flex;align-items:center;justify-content:center}

/* hero */
.hero{position:absolute;left:0;top:0;width:1200px;height:640px;background:linear-gradient(100deg,#1f2f3e 0%,#2d4150 40%,#5c6f7b 65%,#3a4a57 100%)}
.brand{position:absolute;font-family:'Poppins',sans-serif;font-weight:700;letter-spacing:3px;color:#c9ced3}
.nav a{position:absolute;top:49px;font-size:12.5px;color:var(--white);text-decoration:none}
.nav-rule{position:absolute;left:0;top:106px;width:1200px;height:1px;background:rgba(255,255,255,.35)}
.welcome{left:141px;top:234px;font-size:14px;letter-spacing:6px;color:var(--white);font-weight:500}
.hero h1{position:absolute;left:141px;top:262px;width:640px;font-size:38px;line-height:50px;font-weight:700;color:var(--white)}
.hero-sub{left:141px;top:425px;font-size:14px;color:var(--white)}
.dot{position:absolute;left:77px;width:12px;height:12px;border-radius:50%;background:#9aa5ad}
.dot.on{background:var(--green);box-shadow:0 0 0 4px rgba(69,192,135,.35)}

/* why */
.why{position:absolute;left:0;top:640px;width:1200px;height:557px;background:var(--green)}
.sec-title{position:absolute;left:0;width:1200px;text-align:center;font-weight:600;color:var(--ink)}
.feature h3{position:absolute;font-size:18px;font-weight:600}
.feature p{position:absolute;font-size:11.5px;line-height:20px;width:240px}
.feature .rule{position:absolute;width:44px;height:2px}

/* services */
.svc-card{position:absolute;width:275px;height:317px;border-radius:16px;background:var(--card);text-align:center}
.svc-card h4{position:absolute;left:0;width:100%;top:173px;font-size:15.5px;font-weight:600;color:var(--ink)}
.svc-card p{position:absolute;left:20px;width:calc(100% - 40px);top:205px;font-size:11.5px;line-height:20px}
.ring{position:absolute;left:50%;top:64px;width:90px;height:90px;margin-left:-45px;border-radius:50%;border:2px solid var(--green);display:flex;align-items:center;justify-content:center}
.center-text{position:absolute;left:0;width:1200px;text-align:center;font-size:13.5px;line-height:24px}

/* about */
.about-copy p{position:absolute;left:651px;top:2512px;width:430px;font-size:13px;line-height:22.6px;color:var(--text)}

/* testimonials */
.quote{position:absolute;left:557px;top:3174px;width:392px;font-size:13.5px;line-height:24px}

/* footer */
.footer{position:absolute;left:0;top:3720px;width:1200px;height:404px;background:var(--navy-deep)}
.footer h5{position:absolute;top:3792px;font-size:19px;font-weight:600;color:var(--green)}
.footer a{position:absolute;font-size:14px;color:var(--white);text-decoration:none}
.f-text{position:absolute;font-size:14px;color:var(--white);line-height:24px}
.social{position:absolute;top:3913px;width:18px;height:18px;border-radius:50%;border:2px solid var(--white)}
</style>
</head>
<body>

<!-- HERO -->
<section class="hero" role="img" aria-label="Close-up of a CNC milling spindle cutting metal with coolant spray"></section>
<div class="brand" style="left:141px;top:24px;font-size:38px">KORVAL</div>
<nav class="nav">
  <a style="left:688px">Home</a>
  <a style="left:767px">Services</a>
  <a style="left:863px">About Us</a>
</nav>
<div class="btn" style="left:946px;top:38px;width:112px;height:40px">Contact Us</div>
<div class="nav-rule"></div>
<div class="abs welcome">WELCOME TO</div>
<div class="hero"></div>
<h1 class="abs" style="left:141px;top:262px;width:640px;font-size:38px;line-height:50px;font-weight:700;color:#fff">Precision Engineering for Aerospace Defence, and Medical Industries</h1>
<div class="abs hero-sub">Leveraging Modern Technology to Deliver Exceptional Quality</div>
<div class="btn" style="left:141px;top:464px;width:181px;height:40px">Explore Our Services</div>
<div class="dot" style="top:319px"></div>
<div class="dot on" style="top:349px"></div>
<div class="dot" style="top:380px"></div>
<div class="dot" style="top:410px"></div>

<!-- WHY -->
<section class="why"></section>
<svg class="abs" style="left:562px;top:602px" width="76" height="76" viewBox="0 0 76 76">
  <circle cx="38" cy="38" r="36" fill="#fff" stroke="#dfe9e4" stroke-width="2"/>
  <rect x="29" y="22" width="18" height="30" rx="9" fill="none" stroke="#17232e" stroke-width="2.4"/>
  <line x1="38" y1="28" x2="38" y2="34" stroke="#17232e" stroke-width="2.4" stroke-linecap="round"/>
</svg>
<h2 class="sec-title" style="top:714px;font-size:29px;color:#fff">Why Choose Us</h2>

<svg class="abs" style="left:430px;top:792px" width="340" height="312" viewBox="0 0 340 312">
  <polygon points="20,14 300,6 326,290 30,304" fill="#8fdcb7" opacity=".8"/>
  <polygon points="8,40 320,22 332,268 14,296" fill="#a9e6c9" opacity=".7"/>
  <rect x="23" y="21" width="293" height="270" rx="14" fill="#fff"/>
</svg>

<div class="feature" style="color:#fff">
  <svg class="abs" style="left:174px;top:850px" width="62" height="62" viewBox="0 0 62 62" fill="none" stroke="#17232e" stroke-width="2">
    <path d="M8 30 L31 10 L54 30 M14 25 V54 H48 V25"/><circle cx="31" cy="38" r="7"/><path d="M12 10a8 8 0 0 1 8-6M50 10a8 8 0 0 0-8-6"/>
  </svg>
  <h3 style="left:174px;top:925px">Modern facilities</h3>
  <div class="rule" style="left:174px;top:960px;background:#fff"></div>
  <p style="left:174px;top:970px">Lorem ipsum dolor sit amet, consectetur adipiscing elit, sed do eiusmod tempor incididunt ut labore et dolore magna</p>

  <svg class="abs" style="left:486px;top:852px" width="60" height="60" viewBox="0 0 60 60" fill="none" stroke="#17232e" stroke-width="2">
    <rect x="18" y="18" width="24" height="24"/><rect x="24" y="24" width="12" height="12"/>
    <path d="M24 18V6M36 18V6M24 42V54M36 42V54M18 24H6M18 36H6M42 24H54M42 36H54"/>
  </svg>
  <h3 style="left:486px;top:925px;color:#17232e">Advanced Technology</h3>
  <div class="rule" style="left:486px;top:960px;background:#17232e"></div>
  <p style="left:486px;top:970px;color:#17232e">Lorem ipsum dolor sit amet, consectetur adipiscing elit, sed do eiusmod tempor incididunt ut labore et dolore magna</p>

  <svg class="abs" style="left:798px;top:850px" width="60" height="62" viewBox="0 0 60 62" fill="none" stroke="#17232e" stroke-width="2">
    <path d="M6 6H54M14 6V16H46V6M24 16V30L30 38L36 30V16M30 38V48M10 56H50M18 48H42V56"/>
  </svg>
  <h3 style="left:798px;top:925px">Precision Industries</h3>
  <div class="rule" style="left:798px;top:960px;background:#fff"></div>
  <p style="left:798px;top:970px">Lorem ipsum dolor sit amet, consectetur adipiscing elit, sed do eiusmod tempor incididunt ut labore et dolore magna</p>
</div>

<!-- SERVICES -->
<div class="abs" role="img" aria-label="Bright renovated machine shop floor with a blue tool trolley" style="left:0;top:1700px;width:1200px;height:601px;background:linear-gradient(180deg,#ffffff 0%,#e6e9ec 20%,#c9d0d7 45%,#5d7aa3 75%,#2f4f86 100%)"></div>
<h2 class="sec-title" style="top:1272px;font-size:29px">Our Services</h2>
<div class="center-text" style="top:1324px">Lorem ipsum dolor sit amet, consectetur adipiscing elit, sed do eiusmod tempor incididunt ut<br>labore et accumsan lacus vel facilisis.</div>

<div class="svc-card" style="left:141px;top:1414px">
  <div class="ring"><svg width="46" height="46" viewBox="0 0 46 46" fill="none" stroke="#45c087" stroke-width="2"><circle cx="20" cy="26" r="9"/><circle cx="20" cy="26" r="3"/><path d="M26 10H40V18H26ZM33 18V24"/></svg></div>
  <h4>CNC Machining</h4>
  <p>5-axis and 3-axis machining<br>capabilities</p>
</div>
<svg class="abs" style="left:434px;top:1396px" width="330" height="340" viewBox="0 0 330 340">
  <polygon points="40,4 300,12 326,320 8,334" fill="#45c087" opacity=".75"/>
</svg>
<div class="svc-card" role="img" aria-label="EDM wire cutting machine detail" style="left:454px;top:1414px;width:292px;background:linear-gradient(160deg,#31506a,#1b3246 60%,#132434)">
  <div class="ring" style="top:64px"><svg width="46" height="46" viewBox="0 0 46 46" fill="none" stroke="#45c087" stroke-width="2"><path d="M8 12H38M16 12V18H30V12M23 18V30M12 34H34"/></svg></div>
  <h4 style="color:#fff">EDM Wire Cutting</h4>
  <p style="color:#fff">Outline the precision and applications of<br>EDM wire cutting</p>
</div>
<div class="svc-card" style="left:784px;top:1414px">
  <div class="ring"><svg width="46" height="46" viewBox="0 0 46 46" fill="none" stroke="#45c087" stroke-width="2"><rect x="8" y="8" width="30" height="30"/><path d="M14 16H32M23 16V26M16 32H30"/></svg></div>
  <h4>3D Metal Printing</h4>
  <p>innovative approach and advantages of<br>3D metal printing</p>
</div>
<div class="btn" style="left:520px;top:1781px;width:160px;height:41px">View All Service</div>

<!-- ABOUT -->
<div class="abs" role="img" aria-label="CNC spindle machining an aluminium part with metal chips" style="left:0;top:2301px;width:595px;height:579px;background:linear-gradient(135deg,#2a3d5c 0%,#5a7ca8 45%,#9aa7b4 70%,#3b4552 100%)"></div>
<div class="abs" style="left:595px;top:2301px;width:605px;height:579px;background:var(--mint)"></div>
<div class="abs" style="left:651px;top:2425px;font-size:17px;font-weight:500;color:var(--ink)">About Us</div>
<h2 class="abs" style="left:651px;top:2457px;font-size:30px;font-weight:600;color:var(--ink)">Korval CNC Machining Industrial</h2>
<div class="about-copy"><p>Lorem Ipsum is simply dummy text of the printing and typesetting industry. Lorem Ipsum has been the industry's standard dummy text ever since the 1500s, when an unknown printer took a galley of type and scrambled it to make a type specimen book. It has survived not only five centuries, but also the leap into electronic typesetting, remaining essentially unchanged. It was popularised in the 1960s with the release of PageMaker including versions of Lorem Ipsum.</p></div>
<div class="btn" style="left:651px;top:2710px;width:107px;height:40px">Read More</div>

<!-- TESTIMONIALS -->
<h2 class="sec-title" style="top:2957px;font-size:29px">Client Testimonials</h2>
<div class="center-text" style="top:3009px">Lorem ipsum dolor sit amet, consectetur adipiscing elit, sed do eiusmod tempor incididunt ut<br>labore et accumsan lacus vel facilisis.</div>

<div class="abs" style="left:-20px;top:3128px;width:111px;height:371px;background:#fff;border-radius:14px;box-shadow:0 4px 18px rgba(0,0,0,.08)"></div>
<div class="abs" style="left:0;top:3366px;width:38px;height:1px;background:#aab3b9"></div>
<div class="abs" style="left:1107px;top:3128px;width:120px;height:371px;background:var(--green);border-radius:14px"></div>

<svg class="abs" style="left:180px;top:3090px" width="850" height="440" viewBox="0 0 850 440">
  <polygon points="50,18 760,44 824,404 10,420" fill="#c7eedb"/>
  <polygon points="34,42 800,30 812,396 24,410" fill="#a6e3c5" opacity=".7"/>
  <rect x="18" y="38" width="804" height="371" rx="14" fill="#fff" style="filter:drop-shadow(0 4px 12px rgba(0,0,0,.08))"/>
  <path d="M32 38 H80 A210 185 0 0 1 80 409 H32 A14 14 0 0 1 18 395 V52 A14 14 0 0 1 32 38Z" fill="#45c087"/>
</svg>
<div class="abs" role="img" aria-label="Client portrait" style="left:362px;top:3242px;width:144px;height:144px;border-radius:50%;border:4px solid #fff;background:linear-gradient(160deg,#c9cfd4,#5d6670)"></div>
<p class="quote">Lorem ipsum dolor sit amet, consectetur adipiscing elit, sed do eiusmod tempor incididunt ut labore et dolore magna aliqua. Quis ipsum suspendisse ultrices gravida. Risus commodo viverra maecenas accumsan lacus vel facilisis Lorem ipsum dolor sit amet, consectetur adipiscing elit, sed do eiusmod tempor incididunt ut labore et dolore magna aliqua.</p>
<div class="abs" style="left:557px;top:3365px;width:392px;height:1px;background:#aab3b9"></div>
<div class="abs" style="left:557px;top:3383px;font-size:17px;font-weight:600;color:var(--ink)">Dane Morrow</div>
<div class="abs" style="left:557px;top:3412px;font-size:11.5px;line-height:19px">Lorem Ipsum is simply dummy<br>text of the printing</div>

<svg class="abs" style="left:848px;top:3583px" width="142" height="56" viewBox="0 0 142 56">
  <circle cx="29" cy="28" r="27" fill="#fff" stroke="#17232e" stroke-width="2"/>
  <path d="M33 19 L24 28 L33 37" fill="none" stroke="#17232e" stroke-width="2.4" stroke-linecap="round"/>
  <circle cx="112" cy="28" r="28" fill="#45c087"/>
  <path d="M108 19 L117 28 L108 37" fill="none" stroke="#fff" stroke-width="2.4" stroke-linecap="round"/>
</svg>

<!-- FOOTER -->
<footer class="footer"></footer>
<div class="brand" style="left:138px;top:3820px;font-size:40px">KORVAL</div>
<span class="social" style="left:137px" aria-label="Social profile"></span>
<span class="social" style="left:183px" aria-label="Social profile"></span>
<span class="social" style="left:234px" aria-label="Social profile"></span>
<span class="social" style="left:285px" aria-label="Social profile"></span>

<h5 style="position:absolute;left:394px;top:3792px;font-size:19px;font-weight:600;color:var(--green)">Userful Links</h5>
<a class="abs" style="left:394px;top:3848px;font-size:14px;color:#fff">Home</a>
<a class="abs" style="left:394px;top:3894px;font-size:14px;color:#fff">About Us</a>
<a class="abs" style="left:394px;top:3939px;font-size:14px;color:#fff">Services</a>

<h5 style="position:absolute;left:614px;top:3792px;font-size:19px;font-weight:600;color:var(--green)">Other Links</h5>
<a class="abs" style="left:614px;top:3848px;font-size:14px;color:#fff">CNC Machining</a>
<a class="abs" style="left:614px;top:3894px;font-size:14px;color:#fff">EDM Wire Cutting</a>
<a class="abs" style="left:614px;top:3939px;font-size:14px;color:#fff">3D Metal Printing</a>

<h5 style="position:absolute;left:821px;top:3792px;font-size:19px;font-weight:600;color:var(--green)">Contact Us</h5>
<svg class="abs" style="left:821px;top:3851px" width="18" height="20" viewBox="0 0 18 20"><path d="M9 1a7 7 0 0 0-7 7c0 5 7 11 7 11s7-6 7-11a7 7 0 0 0-7-7z" fill="#fff"/><circle cx="9" cy="8" r="2.6" fill="#152a3b"/></svg>
<div class="f-text" style="left:850px;top:3846px">Lorem Ipsum is simply dummy text<br>of the printing.</div>
<svg class="abs" style="left:821px;top:3922px" width="18" height="18" viewBox="0 0 24 24"><path d="M6.6 10.8a15 15 0 0 0 6.6 6.6l2.2-2.2c.3-.3.7-.4 1-.2 1.1.4 2.3.6 3.6.6.6 0 1 .4 1 1V20c0 .6-.4 1-1 1C10.6 21 3 13.4 3 4c0-.6.4-1 1-1h3.5c.6 0 1 .4 1 1 0 1.3.2 2.5.6 3.6.1.3 0 .7-.2 1z" fill="#fff"/></svg>
<div class="f-text" style="left:850px;top:3919px">(123) 456-7890</div>
<svg class="abs" style="left:821px;top:3969px" width="18" height="18" viewBox="0 0 24 24"><path d="M2 11 22 2 15 22 11 13Z" fill="#fff"/></svg>
<div class="f-text" style="left:850px;top:3966px">info@korvaltooling.example</div>

<div class="abs" style="left:78px;top:4035px;width:1062px;height:1px;background:rgba(255,255,255,.35)"></div>
<div class="abs" style="left:0;top:4068px;width:1200px;text-align:center;font-size:12.5px;font-weight:500;color:#fff">© 2024 Korval CNC Machining Industrial . All Rights Reserved.</div>

</body>
</html>
```